Design for Pediatric Occupational Therapist who works with children with special needs

I need 2 x 2 sq business cards and post cards for my Pediatric Occupational Therapy business. We work with children with special needs and help them learn skills for daily living (eating, writing, dressing, etc). We're looking for a colorful design (not loud) that looks professional and helps it stand out from other cards. I want to avoid many of the standard designs that you see on Nimbo press which are used my many other Pediatric OT's. The design will be intended for business cards, post cards and hopefully can also be used on company letterhead. I'll upload a current copy of the logo we currently use on company letter head so you get an idea of the design we've been using to date. This image does not need to be used again, but serves more as a reference to the design used in the past. The winning designer will likely be hired to design a custom logo for letter head.
Updates

Project Deadline Extended Reason: I want to extend the deadline to allow for more designs and review time. Added Sunday, January 8, 2017

Target Market(s)

Families of children with special needs, pediatricians

Industry/Entity Type

Business

Contact Information for Business Card

I need a logo or design for 2 x 2 sq business cards and post cards for my Pediatric Occupational Therapy business. We work with children with special needs and help them learn skills for daily living (eating, writing, dressing, etc). We're looking for a colorful design (not loud) that looks professional and helps it stand out from other cards. I want to avoid many of the standard designs that you see on Nimbo press which are used my many other Pediatric OT's. The design will be intended for business cards, post cards and hopefully can also be used on company letterhead. I'll upload a current copy of the logo we currently use on company letter head so you get an idea of the design we've been using to date.

Font styles to use
Sans Serif

Requirements
Must have
• Area to include company name, address, phone, etc.
• Company name = Meadowlark Therapy Partners

```html
<!DOCTYPE html>
<html lang="en">
<head>
<meta charset="utf-8">
<title>Pediatric Occupational Therapist – Business Card</title>
<link rel="stylesheet" href="https://fonts.googleapis.com/css2?family=Quicksand:wght@500;600;700&display=swap">
<style>
  :root {
    --bg: #2f3d45;
    --card: #ffffff;
    --blue: #1a6fb5;
    --green: #9cc72c;
    --ink: #5b5e62;
  }
  * { box-sizing: border-box; margin: 0; padding: 0; }
  html, body {
    width: 1200px; height: 900px; overflow: hidden;
    background: var(--bg);
    font-family: "Quicksand", sans-serif;
  }
  .card {
    position: absolute;
    left: 270px;
    width: 660px; height: 380px;
    background: var(--card);
    border-radius: 2px;
    overflow: hidden;
  }
  .card--front { top: 50px; }
  .card--back { top: 470px; }

  .wordmark {
    font-family: "Quicksand", sans-serif;
    font-weight: 700;
    color: var(--blue);
    line-height: 1.1;
  }
  .wordmark__line { display: block; }

  .card--front .wordmark {
    position: absolute; left: 0; top: 38px;
    width: 100%;
    text-align: center;
    font-size: 32px;
  }

  .kids-strip {
    position: absolute; left: 130px; top: 175px;
    width: 400px; height: 64px;
  }

  .card--back .wordmark {
    position: absolute; left: 62px; top: 112px;
    font-size: 36px;
  }

  .contact {
    position: absolute; left: 370px; top: 58px;
    color: var(--ink);
    letter-spacing: 0.6px;
  }
  .contact__name { color: var(--blue); font-size: 21px; font-weight: 700; }
  .contact__role { font-size: 15px; font-weight: 600; margin-top: 2px; }
  .contact__tagline { font-size: 16px; font-weight: 600; line-height: 1.45; margin-top: 26px; }
  .contact__list { list-style: none; margin-top: 22px; font-size: 17px; font-weight: 600; line-height: 1.45; }
  .contact__label { color: var(--blue); display: inline-block; width: 26px; }

  .card__bar {
    position: absolute; left: 0; bottom: 0;
    width: 100%; height: 7px; display: flex;
  }
  .card__bar-blue { flex: 1; background: var(--blue); }
  .card__bar-green { flex: 1; background: var(--green); margin-left: 3px; }
</style>
</head>
<body>

<section class="card card--front">
  <h1 class="wordmark">
    <span class="wordmark__line">Pediatric</span>
    <span class="wordmark__line">Occupational</span>
    <span class="wordmark__line">Therapist</span>
  </h1>
  <svg class="kids-strip" viewBox="0 0 400 64" role="img" aria-label="Illustration of a row of children holding hands">
    <defs>
      <linearGradient id="kidsTone" x1="0" x2="1">
        <stop offset="0" stop-color="#8cc63f"/>
        <stop offset="0.3" stop-color="#e94b8a"/>
        <stop offset="0.55" stop-color="#f7a823"/>
        <stop offset="0.8" stop-color="#4fb3e0"/>
        <stop offset="1" stop-color="#8e5bb5"/>
      </linearGradient>
    </defs>
    <rect width="400" height="64" rx="8" fill="url(#kidsTone)" opacity="0.55"/>
  </svg>
</section>

<section class="card card--back">
  <div class="wordmark">
    <span class="wordmark__line">Pediatric</span>
    <span class="wordmark__line">Occupational</span>
    <span class="wordmark__line">Therapist</span>
  </div>

  <div class="contact">
    <p class="contact__name">Person Name</p>
    <p class="contact__role">Designation</p>
    <p class="contact__tagline">Lorem ipsum dolor sit amet<br>Donec accumsan.</p>
    <ul class="contact__list">
      <li><span class="contact__label">p:</span>123 456 7890</li>
      <li><span class="contact__label">f:</span>123 456 7890</li>
      <li><span class="contact__label">e:</span>info@brightot.com</li>
      <li><span class="contact__label">w:</span>www.brightot.com</li>
    </ul>
  </div>

  <div class="card__bar">
    <span class="card__bar-blue"></span>
    <span class="card__bar-green"></span>
  </div>
</section>

</body>
</html>
```